Business Card for Yachting Management Company

Need a business card design for a new yachting project management company. Attached is the logo for the company.
Our clients are large yacht owners and captains.
Design must be in the style of the logo. Modern, elegant.

Example of data to show:
Peter Hollis
Project Manager
(+34) 612 738 104
peter@quorvane.net
Quorvane Management - Meridel Tower, Office 22 - KRB - Palma de Mallorca

The data above will have to be changed (by me) for the different people in the company over the next years.

Will be printed using PrintNova (Lustre Card Series). They provide these guidelines for the size:
"the actual size of the card is 1050 x 600 pixels. However, the full bleed size is 1083 x 633 pixels, and the safe printing area is 1008 x 558 pixels."

```html
<!DOCTYPE html>
<html lang="en">
<head>
<meta charset="utf-8">
<title>Peter Hollis – Business Card</title>
<link rel="stylesheet" href="https://fonts.googleapis.com/css2?family=Montserrat:wght@400&family=Open+Sans:wght@400&display=swap">
<style>
  :root {
    --ink: #3a8ec6;
    --sea-deep: #1580c8;
    --sea-mid: #6fbde6;
    --sea-light: #cfeafa;
    --foam: #f3f9fd;
    --paper: #ffffff;
  }
  html, body {
    margin: 0;
    padding: 0;
    overflow: hidden;
    background: var(--paper);
  }
  .card {
    position: relative;
    width: 1200px;
    height: 706px;
    overflow: hidden;
    background: var(--foam);
    font-family: "Open Sans", Arial, sans-serif;
    color: var(--ink);
  }
  .card__sea {
    position: absolute;
    left: 0;
    top: 0;
    width: 620px;
    height: 706px;
    background:
      linear-gradient(90deg,
        var(--sea-deep) 0%,
        #2a93d2 10%,
        var(--sea-mid) 22%,
        #a9dbf4 38%,
        var(--sea-light) 55%,
        rgba(243, 249, 253, 0.6) 80%,
        rgba(243, 249, 253, 0) 100%);
  }
  .card__panel {
    position: absolute;
    left: 550px;
    top: 0;
    width: 582px;
    height: 634px;
    background: var(--paper);
  }
  .card__name {
    position: absolute;
    left: 617px;
    top: 112px;
    margin: 0;
    font-family: "Montserrat", Arial, sans-serif;
    font-weight: 400;
    font-size: 60px;
    line-height: 1.1;
    letter-spacing: 0.5px;
  }
  .card__role {
    position: absolute;
    left: 619px;
    top: 182px;
    margin: 0;
    font-size: 33px;
    line-height: 1.2;
    font-weight: 400;
  }
  .contact {
    position: absolute;
    left: 617px;
    display: flex;
    align-items: center;
    gap: 11px;
    font-size: 22px;
  }
  .contact--phone { top: 360px; }
  .contact--email { top: 407px; }
  .contact__icon {
    width: 34px;
    height: 34px;
    flex: none;
  }
  .card__address {
    position: absolute;
    left: 619px;
    top: 477px;
    margin: 0;
    font-style: normal;
    font-size: 24px;
    line-height: 35px;
  }
</style>
</head>
<body>
  <div class="card">
    <div class="card__sea" role="img" aria-label="Abstract flowing blue marbled water pattern"></div>
    <div class="card__panel"></div>

    <h1 class="card__name">Peter Hollis</h1>
    <p class="card__role">Project Manager</p>

    <div class="contact contact--phone">
      <svg class="contact__icon" viewBox="0 0 34 34" aria-hidden="true">
        <circle cx="17" cy="17" r="17" fill="var(--ink)"/>
        <path d="M12.2 9.5c.6-.4 1.4-.3 1.8.3l1.7 2.5c.4.6.3 1.3-.2 1.8l-1 .9c.8 1.9 2.3 3.5 4.2 4.4l.9-1c.5-.5 1.2-.6 1.8-.2l2.5 1.6c.6.4.8 1.2.4 1.8l-.9 1.5c-.6 1-1.8 1.4-2.9 1.1-4.6-1.5-8.1-5-9.6-9.6-.3-1.1.1-2.3 1.1-2.9z" fill="#fff"/>
      </svg>
      <span>(+34) 612 738 104</span>
    </div>

    <div class="contact contact--email">
      <svg class="contact__icon" viewBox="0 0 34 34" aria-hidden="true">
        <circle cx="17" cy="17" r="17" fill="var(--ink)"/>
        <rect x="9" y="11.5" width="16" height="11" fill="none" stroke="#fff" stroke-width="1.6"/>
        <path d="M9 11.5l8 6.5 8-6.5M9 22.5l6-5M25 22.5l-6-5" fill="none" stroke="#fff" stroke-width="1.4"/>
      </svg>
      <span>peter@quorvane.net</span>
    </div>

    <address class="card__address">
      Quorvane Management - Meridel Tower,<br>
      Office 22 - KRB - Palma de Mallorca
    </address>
  </div>
</body>
</html>
```